Refer a Friend A5 Flyer for Healthcare Staff

We need an A5 flyer that we can hand out to existing and new staff members promoting our Refer a friend Scheme. We need the leaflet to encourage staff to talk to their family and friends about joining our Healthcare Agency, which provides staff to local care related establishments. Using our logo and brand colours blue and green, as per our website, the final design will need to clearly convey the benefits and attractions of referring additional staff to the team. In addition is the promotion of our our Page page, requesting staff to like the page and to like and share various posts.

Target Market(s)

Healthcare and potential Healthcare Staff

Industry/Entity Type

Healthcare

Colors
33b8a4
3277b5

Requirements
Must have
• Company Logo, Brand colours,
• text; "Refer a Friend and receive a £50 Bonus after just 1 completed shift"
• text; "3 easy steps to refer a friend, 1 Fill out your name on the back of your Business Card 2 Hand the card to your friend or any person you wish to refer, 3 ask your friend to present the card to us when they attend their interview"
• text; "Like and share any of our Open Days on our Page for a chance to win a prize, you can find us easily by searching @CarewellPlacementGroup"
• text; "Like our Page to stay up to date with our events and offers"
Nice to have
• care worker / elderly care / support worker pictures
• Content / pics from website www.carewellplacementgroup.co.uk

```html
<!DOCTYPE html>
<html lang="en">
<head>
<meta charset="utf-8">
<title>Carewell Placement – Refer a Friend Flyer Options</title>
<link href="https://fonts.googleapis.com/css2?family=Oswald:wght@400;500;600&family=Roboto+Condensed:wght@400;700&family=Roboto:wght@400&display=swap" rel="stylesheet">
<style>
  :root {
    --brand-blue: #1a4fa3;
    --brand-green: #14a88c;
    --board-bg: #d3dee6;
    --white: #ffffff;
    --ink: #4a4a4a;
  }
  * { margin: 0; padding: 0; box-sizing: border-box; }
  html, body { width: 1200px; height: 902px; overflow: hidden; }
  body { background: var(--board-bg); position: relative; font-family: "Roboto", sans-serif; }

  .flyer {
    position: absolute; top: 28px; width: 561px; height: 794px;
    background: var(--white); overflow: hidden;
    box-shadow: 0 4px 12px rgba(0,0,0,0.25);
  }
  .flyer--one { left: 30px; }
  .flyer--two { left: 610px; }

  .option-label {
    position: absolute; top: 838px; width: 561px; text-align: center;
    font-family: "Oswald", sans-serif; font-weight: 500; font-size: 45px;
    color: var(--brand-blue); letter-spacing: 0.5px;
  }
  .option-label--one { left: 30px; }
  .option-label--two { left: 610px; }

  .brand-name { position: absolute; left: 24px; top: 40px; display: flex; align-items: center; gap: 10px; }
  .brand-dot { width: 22px; height: 22px; border-radius: 50%; background: var(--brand-green); }
  .brand-text { font-size: 34px; line-height: 36px; color: var(--brand-blue); }

  .visit-pill {
    position: absolute; left: 364px; top: 27px; width: 117px; height: 37px;
    border: 3px solid var(--brand-blue); border-radius: 20px;
    font-family: "Oswald", sans-serif; font-size: 21px; color: var(--brand-green);
    text-align: center; line-height: 30px; letter-spacing: 1px;
  }
  .site-url { position: absolute; left: 300px; top: 76px; width: 260px; text-align: center; font-size: 14px; color: var(--ink); }

  .hero-art { position: absolute; left: 0; top: 110px; }

  .headline {
    position: absolute; left: 22px; top: 180px; color: var(--white);
    font-family: "Oswald", sans-serif; font-weight: 400; font-size: 38px; line-height: 41px;
  }
  .bonus-band {
    position: absolute; left: 0; top: 272px; width: 280px; height: 74px;
    background: var(--brand-green); display: flex; align-items: center; padding-left: 20px; gap: 8px;
    color: var(--white); font-family: "Oswald", sans-serif; font-weight: 600;
  }
  .flyer--one .bonus-band { border-top: 2px dashed var(--white); border-bottom: 2px dashed var(--white); clip-path: polygon(0 0, 100% 0, 93% 50%, 100% 100%, 0 100%); }
  .flyer--two .bonus-band { width: 340px; background: linear-gradient(90deg, var(--brand-green) 55%, rgba(20,168,140,0)); }
  .bonus-amount { font-size: 66px; line-height: 1; }
  .bonus-word { font-size: 40px; line-height: 1; }

  .steps-header {
    position: absolute; left: 240px; top: 444px; width: 321px; height: 32px;
    background: var(--brand-green); border-radius: 16px 0 0 16px;
    font-family: "Oswald", sans-serif; font-weight: 500; font-size: 21px; color: var(--white);
    line-height: 32px; text-align: center;
  }
  .step-line { position: absolute; left: 301px; top: 520px; width: 3px; height: 160px; background: var(--brand-green); }
  .step { position: absolute; left: 240px; width: 321px; height: 60px; }
  .step-number { position: absolute; left: 8px; top: 16px; font-family: "Oswald", sans-serif; font-size: 21px; color: var(--brand-green); }
  .step-icon { position: absolute; left: 32px; top: 0; width: 58px; height: 58px; }
  .step-text { position: absolute; left: 106px; top: 0; width: 192px; font-size: 15px; line-height: 19px; color: var(--ink); }
  .step--one { top: 488px; }
  .step--two { top: 570px; }
  .step--three { top: 654px; }

  .gift-icon { position: absolute; left: 22px; top: 430px; }
  .prize-copy { position: absolute; left: 22px; top: 538px; font-family: "Oswald", sans-serif; font-weight: 400; }
  .prize-copy .lead { font-size: 24px; line-height: 26px; color: var(--brand-blue); }
  .prize-copy .sub { font-size: 19px; line-height: 20px; color: var(--brand-blue); }
  .prize-copy .chance { font-size: 26px; line-height: 32px; color: var(--brand-green); }
  .prize-copy .win { font-size: 33px; line-height: 38px; color: var(--brand-green); }

  .social-tab {
    position: absolute; left: 0; top: 664px; width: 258px; height: 72px;
    background: var(--brand-blue); border-radius: 0 60px 0 0;
    clip-path: polygon(0 0, 70% 0, 80% 10%, 100% 100%, 0 100%);
  }
  .social-dot { position: absolute; left: 22px; top: 682px; width: 32px; height: 32px; border-radius: 50%; background: var(--white); }
  .social-copy {
    position: absolute; left: 58px; top: 668px; width: 162px; text-align: center; color: var(--white);
    font-family: "Roboto Condensed", sans-serif; font-size: 15px; line-height: 20px;
  }

  .like-bar {
    position: absolute; left: 0; top: 736px; width: 561px; height: 58px; background: var(--brand-green);
    display: flex; align-items: center; justify-content: center; gap: 10px;
    color: var(--white); font-family: "Roboto Condensed", sans-serif; font-size: 21px; letter-spacing: 3.4px;
  }
</style>
</head>
<body>

<section class="flyer flyer--one">
  <div class="brand-name"><span class="brand-dot"></span><span class="brand-text">Carewell<br>Placement</span></div>
  <div class="visit-pill">Visit us</div>
  <div class="site-url">www.carewellplacementgroup.co.uk</div>

  <svg class="hero-art" width="561" height="390" viewBox="0 0 561 390">
    <defs>
      <linearGradient id="photoTeam" x1="0" y1="0" x2="1" y2="1">
        <stop offset="0" stop-color="#eef3f7"/><stop offset="0.5" stop-color="#9cc3e3"/><stop offset="1" stop-color="#2e6fb8"/>
      </linearGradient>
    </defs>
    <path d="M0 64 H561 V320 H188 L176 300 H0 Z" fill="var(--brand-blue)"/>
    <path d="M383 318 C 280 240 214 180 214 110 C 214 48 258 6 308 6 C 344 6 370 24 383 50 C 396 24 422 6 458 6 C 508 6 552 48 552 110 C 552 180 486 240 383 318 Z" fill="var(--brand-blue)"/>
    <path role="img" aria-label="Photo of a smiling team of doctors and nurses in scrubs and white coats" d="M383 306 C 287 234 224 178 224 112 C 224 56 264 18 310 18 C 344 18 368 38 383 66 C 398 38 422 18 456 18 C 502 18 542 56 542 112 C 542 178 479 234 383 306 Z" fill="url(#photoTeam)"/>
    <path d="M0 300 H142 L158 244 L176 370 L188 320 H561 V329 H194 L177 386 L160 270 L150 309 H0 Z" fill="var(--brand-green)"/>
  </svg>

  <h1 class="headline">Refer a Friend<br>And receive a</h1>
  <div class="bonus-band"><span class="bonus-amount">£50</span><span class="bonus-word">BONUS</span></div>

  <svg class="gift-icon" width="150" height="112" viewBox="0 0 150 112">
    <rect x="62" y="0" width="24" height="20" rx="2" fill="var(--brand-blue)"/>
    <path d="M81 10 l-6 -6 v4 h-6 v4 h6 v4 z" fill="var(--white)"/>
    <path d="M70 78 C 62 50 30 44 32 66 C 33 76 50 78 70 78 Z M78 78 C 86 50 118 44 116 66 C 115 76 98 78 78 78 Z" fill="none" stroke="var(--brand-green)" stroke-width="7"/>
    <rect x="3.5" y="80" width="141" height="28" fill="none" stroke="var(--brand-green)" stroke-width="7"/>
    <rect x="70" y="76" width="8" height="34" fill="var(--brand-green)"/>
  </svg>
  <div class="prize-copy">
    <div class="lead">share any of our</div>
    <div class="sub">Open Days on our Page</div>
    <div class="chance">for a chance to</div>
    <div class="win">WIN A PRIZE</div>
  </div>

  <div class="steps-header">3 EASY STEPS TO REFER A FRIEND</div>
  <div class="step-line"></div>
  <div class="step step--one">
    <span class="step-number">1</span>
    <svg class="step-icon" viewBox="0 0 58 58"><circle cx="29" cy="29" r="29" fill="var(--brand-green)"/><rect x="19" y="15" width="18" height="24" rx="2" fill="none" stroke="#fff" stroke-width="2.5"/><path d="M23 22h10M23 27h10M23 32h7M34 36l9-11" stroke="#fff" stroke-width="2.5"/></svg>
    <p class="step-text">Put your name on the back of your business card and hand to your friend.</p>
  </div>
  <div class="step step--two">
    <span class="step-number">2</span>
    <svg class="step-icon" viewBox="0 0 58 58"><circle cx="29" cy="29" r="29" fill="var(--brand-green)"/><rect x="22" y="13" width="14" height="22" rx="2" fill="#fff"/><path d="M18 30 v10 c0 6 6 8 12 8 h4 c5 0 6-4 6-8 v-8" fill="none" stroke="#fff" stroke-width="2.5"/></svg>
    <p class="step-text">Ask your friend to bring the card with them to their registration.</p>
  </div>
  <div class="step step--three">
    <span class="step-number">3</span>
    <svg class="step-icon" viewBox="0 0 58 58"><circle cx="29" cy="29" r="29" fill="var(--brand-green)"/><circle cx="30" cy="22" r="8" fill="none" stroke="#fff" stroke-width="2.5"/><path d="M14 36 h10 l6 3 h10 l6-4" fill="none" stroke="#fff" stroke-width="2.5"/></svg>
    <p class="step-text">You receive a £50 Bonus after your friend completes just 1 shift.</p>
  </div>

  <div class="social-tab"></div>
  <div class="social-dot"></div>
  <p class="social-copy">You can find us easily<br>by searching<br>@CarewellPlacementGroup</p>

  <div class="like-bar">
    <svg width="34" height="26" viewBox="0 0 34 26"><rect x="1" y="11" width="8" height="14" fill="#fff"/><path d="M12 11 L18 2 c3 0 4 2 3 5 l-1 4 h10 c3 0 3 4 0 4 c3 0 3 4 0 4 c2 0 2 4 -1 4 h-19 z" fill="#fff"/></svg>
    <span>Like our Page to stay up to date</span>
  </div>
</section>

<section class="flyer flyer--two">
  <div class="brand-name"><span class="brand-dot"></span><span class="brand-text">Carewell<br>Placement</span></div>
  <div class="visit-pill">Visit us</div>
  <div class="site-url">www.carewellplacementgroup.co.uk</div>

  <svg class="hero-art" width="561" height="390" viewBox="0 0 561 390">
    <defs>
      <linearGradient id="photoNurse" x1="0" y1="0" x2="1" y2="1">
        <stop offset="0" stop-color="#f1f2f2"/><stop offset="0.55" stop-color="#c9b7a8"/><stop offset="1" stop-color="#2f6db6"/>
      </linearGradient>
    </defs>
    <path d="M0 64 H561 V320 H188 L176 300 H0 Z" fill="var(--brand-blue)"/>
    <path d="M383 318 C 280 240 214 180 214 110 C 214 48 258 6 308 6 C 344 6 370 24 383 50 C 396 24 422 6 458 6 C 508 6 552 48 552 110 C 552 180 486 240 383 318 Z" fill="var(--brand-blue)"/>
    <path role="img" aria-label="Photo of a smiling nurse in blue scrubs with colleagues shaking hands in an office" d="M383 306 C 287 234 224 178 224 112 C 224 56 264 18 310 18 C 344 18 368 38 383 66 C 398 38 422 18 456 18 C 502 18 542 56 542 112 C 542 178 479 234 383 306 Z" fill="url(#photoNurse)"/>
    <path d="M0 300 H142 L158 244 L176 370 L188 320 H561 V329 H194 L177 386 L160 270 L150 309 H0 Z" fill="var(--brand-green)"/>
  </svg>

  <h1 class="headline">Refer a Friend<br>And receive a</h1>
  <div class="bonus-band"><span class="bonus-amount">£50</span><span class="bonus-word">BONUS</span></div>

  <svg class="gift-icon" width="150" height="112" viewBox="0 0 150 112">
    <rect x="62" y="0" width="24" height="20" rx="2" fill="var(--brand-blue)"/>
    <path d="M81 10 l-6 -6 v4 h-6 v4 h6 v4 z" fill="var(--white)"/>
    <path d="M70 78 C 62 50 30 44 32 66 C 33 76 50 78 70 78 Z M78 78 C 86 50 118 44 116 66 C 115 76 98 78 78 78 Z" fill="none" stroke="var(--brand-green)" stroke-width="7"/>
    <rect x="3.5" y="80" width="141" height="28" fill="none" stroke="var(--brand-green)" stroke-width="7"/>
    <rect x="70" y="76" width="8" height="34" fill="var(--brand-green)"/>
  </svg>
  <div class="prize-copy">
    <div class="lead">share any of our</div>
    <div class="sub">Open Days on our Page</div>
    <div class="chance">for a chance to</div>
    <div class="win">WIN A PRIZE</div>
  </div>

  <div class="steps-header">3 EASY STEPS TO REFER A FRIEND</div>
  <div class="step-line"></div>
  <div class="step step--one">
    <span class="step-number">1</span>
    <svg class="step-icon" viewBox="0 0 58 58"><circle cx="29" cy="29" r="29" fill="var(--brand-green)"/><rect x="19" y="15" width="18" height="24" rx="2" fill="none" stroke="#fff" stroke-width="2.5"/><path d="M23 22h10M23 27h10M23 32h7M34 36l9-11" stroke="#fff" stroke-width="2.5"/></svg>
    <p class="step-text">Put your name on the back of your business card and hand to your friend.</p>
  </div>
  <div class="step step--two">
    <span class="step-number">2</span>
    <svg class="step-icon" viewBox="0 0 58 58"><circle cx="29" cy="29" r="29" fill="var(--brand-green)"/><rect x="22" y="13" width="14" height="22" rx="2" fill="#fff"/><path d="M18 30 v10 c0 6 6 8 12 8 h4 c5 0 6-4 6-8 v-8" fill="none" stroke="#fff" stroke-width="2.5"/></svg>
    <p class="step-text">Ask your friend to bring the card with them to their registration.</p>
  </div>
  <div class="step step--three">
    <span class="step-number">3</span>
    <svg class="step-icon" viewBox="0 0 58 58"><circle cx="29" cy="29" r="29" fill="var(--brand-green)"/><circle cx="30" cy="22" r="8" fill="none" stroke="#fff" stroke-width="2.5"/><path d="M14 36 h10 l6 3 h10 l6-4" fill="none" stroke="#fff" stroke-width="2.5"/></svg>
    <p class="step-text">You receive a £50 Bonus after your friend completes just 1 shift.</p>
  </div>

  <div class="social-tab"></div>
  <div class="social-dot"></div>
  <p class="social-copy">You can find us easily<br>by searching<br>@CarewellPlacementGroup</p>

  <div class="like-bar">
    <svg width="34" height="26" viewBox="0 0 34 26"><rect x="1" y="11" width="8" height="14" fill="#fff"/><path d="M12 11 L18 2 c3 0 4 2 3 5 l-1 4 h10 c3 0 3 4 0 4 c3 0 3 4 0 4 c2 0 2 4 -1 4 h-19 z" fill="#fff"/></svg>
    <span>Like our Page to stay up to date</span>
  </div>
</section>

<div class="option-label option-label--one">OPTION 1</div>
<div class="option-label option-label--two">OPTION 2</div>

</body>
</html>
```